Business Card Design for Quillmoreton Carpentry

I need a business card design for my carpentry company Quillmoreton Carpentry. Ive attached files with all information I require on both sides. Look forward to seeing your design.

```html
<!DOCTYPE html>
<html lang="en">
<head>
<meta charset="utf-8">
<title>Quillmoreton Carpentry – Business Card</title>
<link rel="stylesheet" href="https://fonts.googleapis.com/css2?family=Lato:wght@400;700;900&family=Open+Sans:wght@400;600&display=swap">
<style>
  :root {
    --backdrop: #2b2b2b;
    --orange: #f55a24;
    --ink: #1f1f1f;
    --paper: #ffffff;
  }
  html, body {
    margin: 0;
    padding: 0;
    width: 1200px;
    height: 1200px;
    overflow: hidden;
    background: var(--backdrop);
  }
  .canvas {
    position: relative;
    width: 1200px;
    height: 1200px;
  }
  .card {
    position: absolute;
    top: 310px;
    height: 594px;
    overflow: hidden;
  }
  /* Front */
  .card-front {
    left: 234px;
    width: 364px;
    background: var(--paper);
  }
  .brand {
    position: absolute;
    top: 148px;
    left: 0;
    width: 100%;
    display: flex;
    align-items: center;
    justify-content: center;
    gap: 9px;
    font-family: "Lato", sans-serif;
    font-weight: 900;
    font-size: 18px;
    line-height: 24px;
    letter-spacing: 0.4px;
    color: var(--ink);
    text-transform: uppercase;
  }
  .brand-dot {
    width: 9px;
    height: 9px;
    border-radius: 50%;
    background: var(--orange);
    flex: none;
  }
  .phone-band {
    position: absolute;
    top: 226px;
    left: 0;
    width: 100%;
    height: 78px;
    background: var(--orange);
    color: var(--paper);
    font-family: "Open Sans", sans-serif;
    font-size: 34px;
    line-height: 78px;
    text-align: center;
    letter-spacing: 0.3px;
  }
  .tagline {
    position: absolute;
    top: 328px;
    left: 0;
    width: 100%;
    margin: 0;
    font-family: "Lato", sans-serif;
    font-weight: 700;
    font-size: 22px;
    line-height: 32px;
    text-align: center;
    color: var(--ink);
    text-transform: uppercase;
    letter-spacing: -0.4px;
  }
  .front-illustration {
    position: absolute;
    left: 28px;
    bottom: 0;
    width: 308px;
    height: 156px;
    background: linear-gradient(to bottom, #f7b08f, var(--orange) 45%, #3a2a24);
  }
  /* Back */
  .card-back {
    left: 627px;
    width: 369px;
    background: var(--orange);
    color: var(--paper);
    font-family: "Open Sans", sans-serif;
  }
  .back-decoration {
    position: absolute;
    left: 28px;
    bottom: 0;
    width: 313px;
    height: 154px;
    background: rgba(255,255,255,0.05);
  }
  .services {
    position: absolute;
    left: 0;
    width: 100%;
    margin: 0;
    padding: 0;
    list-style: none;
    text-align: center;
    font-size: 17.5px;
    line-height: 27px;
  }
  .services-main { top: 87px; }
  .services-extra { top: 283px; }
  .divider {
    position: absolute;
    top: 263px;
    left: 81px;
    width: 207px;
    height: 2px;
    background: var(--paper);
  }
  .email {
    position: absolute;
    top: 498px;
    left: 0;
    width: 100%;
    text-align: center;
    font-size: 17.5px;
    font-weight: 600;
    line-height: 26px;
  }
  .edge-tab {
    position: absolute;
    top: 493px;
    width: 11px;
    height: 39px;
    background: rgba(255,255,255,0.7);
  }
  .edge-tab-left { left: 0; }
  .edge-tab-right { right: 0; }
</style>
</head>
<body>
<main class="canvas">
  <section class="card card-front">
    <div class="brand"><span class="brand-dot"></span>Quillmoreton Carpentry</div>
    <div class="phone-band">0491570156</div>
    <p class="tagline">Anything Carpentry<br>Anywhere in Sydney</p>
    <div class="front-illustration" role="img" aria-label="Illustration area: saw blade with harbour city landmarks"></div>
  </section>

  <section class="card card-back">
    <div class="back-decoration" role="img" aria-label="Faint background illustration area"></div>
    <ul class="services services-main">
      <li>Decks and Pergolas</li>
      <li>Wall and Roof Framing</li>
      <li>Doors And Windows</li>
      <li>Attic Conversions</li>
      <li>Timber Flooring</li>
      <li>Extensions</li>
    </ul>
    <div class="divider"></div>
    <ul class="services services-extra">
      <li>Shop Fitats</li>
      <li>Refurbishments</li>
      <li>Fences/Gates</li>
      <li>Privacy Screens</li>
      <li>Wall Cladding</li>
      <li>more</li>
    </ul>
    <span class="edge-tab edge-tab-left"></span>
    <div class="email">quillmoretoncarpentry@mail.com</div>
    <span class="edge-tab edge-tab-right"></span>
  </section>
</main>
</body>
</html>
```